Company Website for an IT business called "BRIGHT CORRIDOR"

Complete website creation with text and graphics.
We need :
- modern and creative design for our IT company
- Content management system to edit text later on
- Integrate third party content from partner company
- Contact form (transfer by email)
Updates

Designs look the same

Target Market(s)

Small and medium business
private customers

Industry/Entity Type

Information Technology

Coding

Coded - Design and coding required

Number of Pages Required

1 page

Font styles to use
Sans Serif

Requirements
Must have
• Contact form
Link to legal information
Link to data protection (GDPR)
Link to website owner declaration
Nice to have
• Fresh and creative graphics for IT business

```html
<!DOCTYPE html>
<html lang="en">
<head>
<meta charset="utf-8">
<title>Bright Corridor – IT Business Consulting</title>
<link href="https://fonts.googleapis.com/css2?family=Montserrat:wght@300;400;600;700;800&family=Open+Sans:wght@400;600&display=swap" rel="stylesheet">
<style>
:root{
  --blue:#0a6fe0;
  --blue-deep:#0647b8;
  --blue-dark:#062a86;
  --cyan:#36b7f2;
  --ink:#1c1f26;
  --grey:#6c7280;
  --line:#d7dbe3;
  --black:#050608;
  --white:#ffffff;
  --head:'Montserrat',Arial,sans-serif;
  --body:'Open Sans',Arial,sans-serif;
}
*{box-sizing:border-box;margin:0;padding:0}
html,body{width:1200px;height:3924px;overflow:hidden}
body{font-family:var(--body);color:var(--ink);background:var(--white);position:relative}
section,header,footer{position:absolute;left:0;width:1200px;overflow:hidden}
.btn{display:inline-block;font-family:var(--head);font-weight:700;font-size:13px;letter-spacing:.5px;padding:11px 30px;border-radius:24px;text-decoration:none}
.btn--white{background:var(--white);color:var(--blue)}
.btn--blue{background:var(--blue);color:var(--white)}
.btn--outline{border:1.5px solid var(--blue);color:var(--blue);background:var(--white);padding:8px 26px;font-size:11px}
.btn--ghost{border:1.5px solid var(--white);color:var(--white);padding:10px 28px}

/* Hero */
.hero{top:0;height:720px;background:linear-gradient(120deg,#0c7cf0 0%,#0a5ed8 50%,#0c7cf0 100%)}
.hero__wave{position:absolute;left:0;bottom:0;width:1200px;height:200px}
.brand{position:absolute;font-family:var(--head);font-weight:700;color:var(--white);letter-spacing:1px}
.hero .brand{left:60px;top:42px;font-size:18px}
.nav{position:absolute;top:30px;left:400px;display:flex;gap:62px;font-family:var(--head);font-size:12px;font-weight:600;color:var(--white)}
.nav a{color:var(--white);text-decoration:none;padding-bottom:8px;opacity:.9}
.nav a.is-active{border-bottom:2px solid var(--white);opacity:1}
.hero__title{position:absolute;left:120px;top:258px;font-family:var(--head);color:var(--white);line-height:1.12}
.hero__title b{display:block;font-weight:800;font-size:46px;letter-spacing:1px}
.hero__title span{display:block;font-weight:300;font-size:46px;letter-spacing:1px}
.hero .btn{position:absolute;left:120px;top:434px}
.hero__art{position:absolute;left:500px;top:40px;width:510px;height:510px;border-radius:50%;background:radial-gradient(circle at 50% 45%,#6fd0ff 0%,#1f8af0 45%,#0b3fb8 100%);box-shadow:0 0 0 6px rgba(255,255,255,.15)}
.hero__arrow{position:absolute;top:338px}

/* About */
.about{top:720px;height:592px;background:var(--white)}
.about__photo{position:absolute;left:0;top:20px;width:600px;height:560px;background:linear-gradient(100deg,#eef1f4 0%,#c9ced5 45%,#f3f5f7 100%)}
.section-title{font-family:var(--head);font-size:30px;font-weight:400;color:var(--ink);letter-spacing:.5px}
.section-title b{font-weight:800}
.about .section-title{position:absolute;left:700px;top:128px;text-align:center;width:440px}
.about__text{position:absolute;left:700px;top:182px;width:440px;font-size:12.5px;line-height:1.6;color:var(--grey)}
.hexes{position:absolute;left:640px;top:270px;display:flex;gap:14px}
.hex{width:150px;height:172px;position:relative}
.hex svg{position:absolute;inset:0}
.hex__body{position:absolute;inset:0;display:flex;flex-direction:column;align-items:center;justify-content:center;text-align:center;padding:0 26px}
.hex__label{font-family:var(--head);font-size:10.5px;font-weight:700;margin:8px 0 4px;color:var(--ink)}
.hex__text{font-size:9.5px;line-height:1.4;color:var(--grey)}
.hex--active .hex__label,.hex--active .hex__text{color:var(--white)}

/* Data protection */
.privacy{top:1312px;height:608px;background:linear-gradient(115deg,#0b66d8 0%,#0a4cc0 55%,#0a3aa8 100%)}
.privacy .section-title{position:absolute;left:128px;top:150px;color:var(--white)}
.privacy__text{position:absolute;left:128px;top:200px;width:460px;font-size:12.5px;line-height:1.6;color:#dce9ff}
.features{position:absolute;left:128px;top:268px;display:grid;grid-template-columns:240px 240px;row-gap:30px}
.feature{display:flex;gap:14px;align-items:center;font-size:11px;line-height:1.45;color:#dce9ff}
.privacy .btn{position:absolute;left:128px;top:454px}
.privacy__art{position:absolute;left:610px;top:40px;width:560px;height:500px;border-radius:8px;background:radial-gradient(ellipse at 55% 50%,#5fc6ff 0%,#1d7ae8 45%,rgba(10,60,170,0) 75%)}

/* IT consulting */
.consulting{top:1920px;height:600px;background:var(--black);color:var(--white);text-align:center}
.consulting__notch{position:absolute;left:560px;top:0}
.consulting .section-title{position:absolute;left:0;width:1200px;top:58px;color:var(--white)}
.consulting__text{position:absolute;left:330px;top:112px;width:540px;font-size:12.5px;line-height:1.6;color:#d0d4db}
.consulting__text p+p{margin-top:14px}
.consulting .btn{position:absolute;left:530px;top:248px}
.consulting__art{position:absolute;left:0;top:310px;width:1200px;height:290px;background:radial-gradient(ellipse at 50% 60%,#8a6a3a 0%,#3a2a16 35%,#050608 70%)}

/* Resources */
.resources{top:2520px;height:520px;background:var(--white)}
.resources .section-title{position:absolute;left:0;width:1200px;top:76px;text-align:center}
.res{position:absolute;top:148px;width:260px;text-align:center}
.res__img{width:200px;height:200px;margin:0 auto;clip-path:polygon(50% 0,93% 25%,93% 75%,50% 100%,7% 75%,7% 25%)}
.res__title{font-family:var(--head);font-weight:800;font-size:15px;line-height:1.3;margin:18px 0 16px;color:var(--ink)}

/* Contact */
.contact{top:3040px;height:540px;background:linear-gradient(180deg,#ffffff 0%,#e9f3fb 40%,#dcecf8 100%)}
.contact__art{position:absolute;inset:0;background:radial-gradient(ellipse at 25% 55%,rgba(120,190,240,.35) 0%,rgba(255,255,255,0) 60%)}
.contact .brand{left:150px;top:240px;font-size:34px;color:var(--blue)}
.contact .section-title{position:absolute;left:620px;top:56px}
.form{position:absolute;left:620px;top:110px;width:460px}
.field{display:flex;align-items:center;gap:12px;height:40px;border:1px solid var(--line);background:var(--white);margin-bottom:14px;padding:0 14px;font-size:11px;color:var(--grey);letter-spacing:.4px}
.field--area{height:112px;align-items:flex-start;padding-top:12px}
.form .btn{margin-top:10px;margin-left:0}

/* Footer */
.footer{top:3580px;height:344px;background:var(--black);color:var(--white)}
.footer .brand{left:140px;top:68px;font-size:24px}
.footer__copy{position:absolute;left:140px;top:120px;font-size:10px;color:#8a9099}
.footer__col{position:absolute;top:66px;font-size:11px;line-height:2.1;color:#b8bdc6}
.footer__col h4{font-family:var(--head);font-size:12px;font-weight:700;color:var(--white);margin-bottom:6px;letter-spacing:.5px}
.socials{display:flex;gap:8px;margin-top:10px}
.socials span{width:20px;height:20px;background:var(--white);border-radius:2px}
</style>
</head>
<body>

<header class="hero">
  <svg class="hero__wave" viewBox="0 0 1200 200" preserveAspectRatio="none" aria-hidden="true">
    <path d="M0 120 C300 60 520 170 800 110 C980 70 1100 100 1200 80 L1200 200 L0 200Z" fill="#0a55cc" opacity=".55"/>
    <path d="M0 160 C260 110 560 200 860 150 C1020 125 1120 140 1200 130 L1200 200 L0 200Z" fill="#ffffff"/>
  </svg>
  <div class="brand">BRIGHT CORRIDOR</div>
  <nav class="nav">
    <a class="is-active" href="#about">ABOUT US</a>
    <a href="#consulting">SERVICES</a>
    <a href="#privacy">DATA PROTECTION</a>
    <a href="#resources">NEWS</a>
    <a href="#contact">SUPPORT</a>
    <a href="#contact">CONTACT</a>
  </nav>
  <h1 class="hero__title"><b>BUSINESS</b><b>CONSULTING</b><span>TO THE FUTURE</span></h1>
  <a class="btn btn--white" href="#about">LEARN MORE</a>
  <div class="hero__art" role="img" aria-label="Illustration of a glowing digital brain above a circuit-board chip"></div>
  <svg class="hero__arrow" style="left:24px" width="24" height="24" viewBox="0 0 24 24" aria-hidden="true"><path d="M20 12H4M10 6l-6 6 6 6" stroke="#fff" stroke-width="2" fill="none"/></svg>
  <svg class="hero__arrow" style="left:1152px" width="24" height="24" viewBox="0 0 24 24" aria-hidden="true"><path d="M4 12h16M14 6l6 6-6 6" stroke="#fff" stroke-width="2" fill="none"/></svg>
</header>

<section class="about" id="about">
  <div class="about__photo" role="img" aria-label="Photo of a consultant working on a laptop"></div>
  <h2 class="section-title">ABOUT <b>BRIGHT CORRIDOR</b></h2>
  <p class="about__text">We help growing firms plan, build and run reliable IT, from the first network to secure cloud services, with clear advice and steady support every day.</p>
  <div class="hexes">
    <div class="hex">
      <svg viewBox="0 0 150 172" aria-hidden="true"><polygon points="75,2 147,44 147,128 75,170 3,128 3,44" fill="#fff" stroke="#36b7f2" stroke-width="2"/></svg>
      <div class="hex__body">
        <svg width="26" height="26" viewBox="0 0 26 26" aria-hidden="true"><circle cx="13" cy="9" r="5" fill="none" stroke="#0a6fe0" stroke-width="2"/><path d="M3 24c1-6 5-8 10-8s9 2 10 8" fill="none" stroke="#0a6fe0" stroke-width="2"/></svg>
        <div class="hex__label">EXPERT TEAM</div>
        <div class="hex__text">Short line about our people here.</div>
      </div>
    </div>
    <div class="hex hex--active">
      <svg viewBox="0 0 150 172" aria-hidden="true"><polygon points="75,2 147,44 147,128 75,170 3,128 3,44" fill="#1a9be8"/></svg>
      <div class="hex__body">
        <svg width="26" height="26" viewBox="0 0 26 26" aria-hidden="true"><rect x="3" y="5" width="20" height="13" rx="1" fill="none" stroke="#fff" stroke-width="2"/><path d="M8 22h10" stroke="#fff" stroke-width="2"/></svg>
        <div class="hex__label">CLOUD SETUP</div>
        <div class="hex__text">Short line about our cloud work.</div>
      </div>
    </div>
    <div class="hex">
      <svg viewBox="0 0 150 172" aria-hidden="true"><polygon points="75,2 147,44 147,128 75,170 3,128 3,44" fill="#fff" stroke="#36b7f2" stroke-width="2"/></svg>
      <div class="hex__body">
        <svg width="26" height="26" viewBox="0 0 26 26" aria-hidden="true"><path d="M4 14a9 9 0 0 1 18 0v5h-4v-6h4M4 13h4v6H4z" fill="none" stroke="#0a6fe0" stroke-width="2"/></svg>
        <div class="hex__label">FAST SUPPORT</div>
        <div class="hex__text">Short line about our help desk.</div>
      </div>
    </div>
  </div>
</section>

<section class="privacy" id="privacy">
  <h2 class="section-title">DATA <b>PROTECTION</b></h2>
  <p class="privacy__text">Your data stays yours. We set up secure systems, clear access rules and regular checks so your business meets GDPR duties without extra stress.</p>
  <div class="features">
    <div class="feature"><svg width="26" height="26" viewBox="0 0 26 26" aria-hidden="true"><path d="M13 2l9 4v6c0 6-4 10-9 12-5-2-9-6-9-12V6z" fill="none" stroke="#fff" stroke-width="1.8"/></svg><span>Encrypted storage for<br>every single file</span></div>
    <div class="feature"><svg width="26" height="26" viewBox="0 0 26 26" aria-hidden="true"><rect x="5" y="11" width="16" height="12" rx="1" fill="none" stroke="#fff" stroke-width="1.8"/><path d="M9 11V7a4 4 0 0 1 8 0v4" fill="none" stroke="#fff" stroke-width="1.8"/></svg><span>Clear access rules for<br>each of your staff</span></div>
    <div class="feature"><svg width="26" height="26" viewBox="0 0 26 26" aria-hidden="true"><circle cx="13" cy="13" r="10" fill="none" stroke="#fff" stroke-width="1.8"/><path d="M8 13l4 4 6-8" fill="none" stroke="#fff" stroke-width="1.8"/></svg><span>Regular audits and<br>compliance reports</span></div>
    <div class="feature"><svg width="26" height="26" viewBox="0 0 26 26" aria-hidden="true"><path d="M4 17a6 6 0 0 1 3-11 7 7 0 0 1 13 2 5 5 0 0 1 0 9z" fill="none" stroke="#fff" stroke-width="1.8"/></svg><span>Safe backups kept in<br>secure data centres</span></div>
  </div>
  <a class="btn btn--white" href="#contact">LEARN MORE</a>
  <div class="privacy__art" role="img" aria-label="Isometric illustration of a laptop with a security shield and padlocks"></div>
</section>

<section class="consulting" id="consulting">
  <svg class="consulting__notch" width="80" height="28" viewBox="0 0 80 28" aria-hidden="true"><polygon points="0,0 80,0 40,28" fill="#0a3aa8"/></svg>
  <h2 class="section-title"><b>IT BUSINESS CONSULTING</b></h2>
  <div class="consulting__text">
    <p>We look at how your team works today and build an IT plan that fits your budget, grows with you and keeps daily work running smoothly.</p>
    <p>From hardware and networks to software and training, one partner takes care of it all with honest advice.</p>
  </div>
  <a class="btn btn--ghost" href="#contact">LEARN MORE</a>
  <div class="consulting__art" role="img" aria-label="Photo of a row of glowing light bulbs with consulting keywords inside"></div>
</section>

<section class="resources" id="resources">
  <h2 class="section-title">OUR <b>RESOURCES</b></h2>
  <div class="res" style="left:170px">
    <div class="res__img" role="img" aria-label="Illustration of a website on a screen" style="background:linear-gradient(140deg,#3a2fd6,#1b8ff0)"></div>
    <div class="res__title">WEBSITE OWNER<br>DECLARATION</div>
    <a class="btn btn--outline" href="#">LEARN MORE</a>
  </div>
  <div class="res" style="left:470px">
    <div class="res__img" role="img" aria-label="Illustration of legal documents on a laptop" style="background:linear-gradient(140deg,#5a3ae0,#2aa0f2)"></div>
    <div class="res__title">LEGAL<br>INFORMATION</div>
    <a class="btn btn--outline" href="#">LEARN MORE</a>
  </div>
  <div class="res" style="left:770px">
    <div class="res__img" role="img" aria-label="Illustration of stacked data layers and servers" style="background:linear-gradient(140deg,#1e6be8,#7a3ad8)"></div>
    <div class="res__title">LOREM IPSUM DOLOR<br>SIT AMET</div>
    <a class="btn btn--outline" href="#">LEARN MORE</a>
  </div>
</section>

<section class="contact" id="contact">
  <div class="contact__art" role="img" aria-label="Soft blue network of connected dots in the background"></div>
  <div class="brand">BRIGHT CORRIDOR</div>
  <h2 class="section-title"><b>CONTACT</b> US</h2>
  <form class="form">
    <div class="field"><svg width="14" height="14" viewBox="0 0 14 14" aria-hidden="true"><circle cx="7" cy="4.5" r="3" fill="none" stroke="#6c7280"/><path d="M1 13c1-4 3-5 6-5s5 1 6 5" fill="none" stroke="#6c7280"/></svg>YOUR NAME</div>
    <div class="field"><svg width="14" height="14" viewBox="0 0 14 14" aria-hidden="true"><rect x="1" y="3" width="12" height="8" fill="none" stroke="#6c7280"/><path d="M1 3l6 5 6-5" fill="none" stroke="#6c7280"/></svg>E-MAIL ADDRESS</div>
    <div class="field"><svg width="14" height="14" viewBox="0 0 14 14" aria-hidden="true"><path d="M3 1h3l1 3-2 1a7 7 0 0 0 4 4l1-2 3 1v3a1 1 0 0 1-1 1A11 11 0 0 1 2 2a1 1 0 0 1 1-1z" fill="none" stroke="#6c7280"/></svg>PHONE NUMBER</div>
    <div class="field field--area">MESSAGE</div>
    <a class="btn btn--blue" href="#">SUBMIT ›</a>
  </form>
</section>

<footer class="footer">
  <div class="brand">BRIGHT CORRIDOR</div>
  <p class="footer__copy">Copyright © 2024 Bright Corridor. All rights reserved.</p>
  <div class="footer__col" style="left:468px">
    <h4>COMPANY</h4>
    About Us<br>Data Protection<br>IT Business Consulting<br>Projects
  </div>
  <div class="footer__col" style="left:700px">
    <h4>RESOURCES</h4>
    Case Results<br>News<br>Blog<br>Contact Us
  </div>
  <div class="footer__col" style="left:888px">
    <h4>CONTACT US</h4>
    Telephone: (555) 010-2044<br>info@brightcorridor.example
    <div class="socials"><span></span><span></span><span></span><span></span></div>
  </div>
</footer>

</body>
</html>
```